Design the app for the next Dwelvo

We need a cutting edge, super UX-intuitive, design for a global parking app called Sloto.
- Homescreen and website have been finalised already (see attached pdf)
- Wireframed screens for the concepts we need have been provided in the attached pdf
- We need some really nice icons for parking space types, etc
- Needs to be very, very intuitive to use and navigate.
References: Dwelvo app & Zipto app, for their simplicity of use
Reason: A few designers have requested that we extend this deadline. So here you go.
Parking

```html
<!DOCTYPE html>
<html lang="en">
<head>
<meta charset="utf-8">
<title>Sloto – Welcome and Onboarding</title>
<link rel="stylesheet" href="https://fonts.googleapis.com/css2?family=Raleway:wght@300;400;500;600&display=swap">
<style>
  :root {
    --canvas-bg: #e9ebed;
    --ink: #1e1f22;
    --muted: #8a8d92;
    --white: #ffffff;
    --accent: #f25c5c;
    --dot-idle: #e6e7e9;
    --hero-top: #3b4552;
    --hero-mid: #2f3a49;
    --hero-bottom: #3a4656;
    --art-light: #b9e2ec;
    --art-mid: #9ccfdd;
  }
  * { box-sizing: border-box; margin: 0; padding: 0; }
  html, body { width: 1200px; height: 1025px; overflow: hidden; }
  body {
    background: var(--canvas-bg);
    font-family: "Raleway", sans-serif;
    position: relative;
  }
  .screen {
    position: absolute;
    top: 115px;
    width: 450px;
    height: 795px;
    overflow: hidden;
    box-shadow: 0 12px 40px rgba(0,0,0,0.12);
  }
  .screen--welcome { left: 100px; }
  .screen--onboarding { left: 650px; background: var(--white); }

  .status-bar {
    position: absolute; top: 8px; left: 16px; right: 16px;
    display: flex; justify-content: space-between; align-items: center;
    font-size: 14px; font-weight: 500;
  }
  .screen--welcome .status-bar { color: var(--white); }
  .screen--onboarding .status-bar { color: var(--ink); }
  .status-bar__left, .status-bar__right { display: flex; align-items: center; gap: 5px; }
  .status-bar__time { position: absolute; left: 50%; transform: translateX(-50%); }

  .hero-photo {
    position: absolute; inset: 0;
    background:
      linear-gradient(115deg, rgba(255,255,255,0) 48%, rgba(255,255,255,0.06) 48%, rgba(255,255,255,0.06) 100%),
      linear-gradient(180deg, var(--hero-top) 0%, var(--hero-mid) 45%, var(--hero-bottom) 100%);
  }
  .login-button {
    position: absolute; top: 48px; left: 372px;
    width: 56px; height: 22px;
    background: var(--accent); color: var(--white);
    border-radius: 2px;
    font-size: 11px; font-weight: 500;
    display: flex; align-items: center; justify-content: center;
  }
  .brand {
    position: absolute; top: 245px; left: 0; right: 0;
    text-align: center; color: var(--white);
  }
  .brand__name {
    font-size: 34px; font-weight: 300; letter-spacing: 14px;
    padding-left: 14px;
  }
  .brand__tagline {
    margin-top: 12px;
    font-size: 12px; font-weight: 300; color: rgba(255,255,255,0.75);
  }
  .outline-button {
    position: absolute; left: 68px; width: 316px; height: 47px;
    border: 2px solid rgba(255,255,255,0.85);
    color: var(--white);
    font-size: 13px; font-weight: 600;
    display: flex; align-items: center; justify-content: center;
    text-transform: uppercase;
  }
  .outline-button--lease { top: 536px; }
  .outline-button--search { top: 623px; }

  .onboarding-art {
    position: absolute; left: 128px; top: 128px;
    width: 194px; height: 194px; border-radius: 50%;
    background: linear-gradient(160deg, var(--art-light) 0%, var(--art-mid) 100%);
  }
  .onboarding-title {
    position: absolute; top: 366px; left: 0; right: 0;
    text-align: center;
    font-size: 19px; font-weight: 500; line-height: 24px; color: var(--ink);
  }
  .onboarding-copy {
    position: absolute; top: 452px; left: 68px; right: 68px;
    text-align: center;
    font-size: 13.5px; line-height: 16.5px; color: var(--muted);
  }
  .onboarding-copy p + p { margin-top: 16px; }
  .pager {
    position: absolute; top: 675px; left: 160px;
    display: flex; align-items: center;
  }
  .pager__dot {
    width: 16px; height: 16px; border-radius: 50%;
    background: var(--dot-idle);
    margin-right: 34px;
  }
  .pager__dot--active { width: 26px; height: 26px; background: var(--accent); margin-right: 30px; }
</style>
</head>
<body>

<section class="screen screen--welcome">
  <div class="hero-photo" role="img" aria-label="Dimmed street photo of a dark blue car parked beside city buildings"></div>

  <div class="status-bar">
    <div class="status-bar__left">
      <svg width="40" height="8" viewBox="0 0 40 8"><g fill="currentColor"><circle cx="4" cy="4" r="3.5"/><circle cx="12" cy="4" r="3.5"/><circle cx="20" cy="4" r="3.5"/></g><g fill="none" stroke="currentColor"><circle cx="28" cy="4" r="3"/><circle cx="36" cy="4" r="3"/></g></svg>
      <span>NOVO</span>
      <svg width="14" height="10" viewBox="0 0 14 10"><path d="M1 3.5a9 9 0 0 1 12 0M3.3 5.8a5.5 5.5 0 0 1 7.4 0M7 9.5l1.8-1.8a2.5 2.5 0 0 0-3.6 0z" fill="none" stroke="currentColor" stroke-width="1.5"/></svg>
    </div>
    <span class="status-bar__time">4:21 PM</span>
    <div class="status-bar__right">
      <svg width="8" height="12" viewBox="0 0 8 12"><path d="M1 3l6 5-3 3V1l3 3-6 5" fill="none" stroke="currentColor" stroke-width="1"/></svg>
      <span>100%</span>
      <svg width="30" height="12" viewBox="0 0 30 12"><rect x="0.5" y="0.5" width="26" height="11" rx="2" fill="none" stroke="currentColor"/><rect x="2" y="2" width="23" height="8" fill="currentColor"/><rect x="27.5" y="4" width="2" height="4" fill="currentColor"/></svg>
    </div>
  </div>

  <div class="login-button">Login</div>

  <div class="brand">
    <div class="brand__name">SLOTO</div>
    <div class="brand__tagline">your private parking space</div>
  </div>

  <div class="outline-button outline-button--lease">Lease your parking space</div>
  <div class="outline-button outline-button--search">Search for parking</div>
</section>

<section class="screen screen--onboarding">
  <div class="status-bar">
    <div class="status-bar__left">
      <svg width="40" height="8" viewBox="0 0 40 8"><g fill="currentColor"><circle cx="4" cy="4" r="3.5"/><circle cx="12" cy="4" r="3.5"/><circle cx="20" cy="4" r="3.5"/></g><g fill="none" stroke="currentColor"><circle cx="28" cy="4" r="3"/><circle cx="36" cy="4" r="3"/></g></svg>
      <span>NOVO</span>
      <svg width="14" height="10" viewBox="0 0 14 10"><path d="M1 3.5a9 9 0 0 1 12 0M3.3 5.8a5.5 5.5 0 0 1 7.4 0M7 9.5l1.8-1.8a2.5 2.5 0 0 0-3.6 0z" fill="none" stroke="currentColor" stroke-width="1.5"/></svg>
    </div>
    <span class="status-bar__time">4:21 PM</span>
    <div class="status-bar__right">
      <svg width="8" height="12" viewBox="0 0 8 12"><path d="M1 3l6 5-3 3V1l3 3-6 5" fill="none" stroke="currentColor" stroke-width="1"/></svg>
      <span>100%</span>
      <svg width="30" height="12" viewBox="0 0 30 12"><rect x="0.5" y="0.5" width="26" height="11" rx="2" fill="none" stroke="currentColor"/><rect x="2" y="2" width="23" height="8" fill="currentColor"/><rect x="27.5" y="4" width="2" height="4" fill="currentColor"/></svg>
    </div>
  </div>

  <div class="onboarding-art" role="img" aria-label="Round illustration of a red car parked by a parking sign in front of a city skyline"></div>

  <h2 class="onboarding-title">Locate an affordable<br>parking space near you</h2>

  <div class="onboarding-copy">
    <p>Find someone who has an empty space where you can park your car, motrobike, boat or helicopter.</p>
    <p>This might be an empty driveway, a garage, a boat mooringor a even a building rooftop.</p>
  </div>

  <div class="pager">
    <span class="pager__dot pager__dot--active"></span>
    <span class="pager__dot"></span>
    <span class="pager__dot"></span>
  </div>
</section>

</body>
</html>
```